Roofing company door hanger
Door hanger design double sided
Update, if possible, lenghten door hanger to allow for business card slot. Thank you.
DESIGNERS WHO ARE WORKING ON THIS CAN ALSO SUBMIT BUSINESS CARD AND STATIONERY ON OUR OTHER PROJECT. WE WOULD LIKE A CONSISTENT LOOK SO PLEASE KEEP THAT IN MIND
HERE IS THE PROJECT LINK:
http://www.plenavox.com/contests/business-card-and-letterhead-4
BEST OF LUCK!!!

```html
<!DOCTYPE html>
<html lang="en">
<head>
<meta charset="utf-8">
<title>Keystone Builders – Door Hanger</title>
<link href="https://fonts.googleapis.com/css2?family=Montserrat:wght@600;700;800&family=Open+Sans:wght@400;600;700&display=swap" rel="stylesheet">
<style>
:root{
  --bg:#2f2b29;
  --red:#c9171e;
  --red-bright:#e0252c;
  --red-deep:#7c0a0e;
  --white:#ffffff;
  --cream:#f3ece4;
  --ink:#2a2a2a;
  --label:#ffffff;
  --photo-house-a:#9a8a74;
  --photo-house-b:#5d6a4e;
  --photo-sky:#b9c8d4;
}
*{margin:0;padding:0;box-sizing:border-box}
html,body{width:1200px;height:574px;overflow:hidden;background:var(--bg)}
body{position:relative;font-family:"Open Sans",Arial,sans-serif;color:var(--white)}

.view-label{position:absolute;top:14px;font-family:"Montserrat",Arial,sans-serif;font-weight:700;font-size:15px;color:var(--label);white-space:nowrap}

.hanger{position:absolute;top:77px;height:480px;overflow:hidden;background:linear-gradient(180deg,var(--red-bright) 0%,var(--red) 45%,var(--red-deep) 100%)}
.hanger-hole{position:absolute;top:22px;left:50%;width:46px;height:46px;margin-left:-23px;border-radius:50%;background:var(--bg);z-index:3}

.brand{display:flex;align-items:center;gap:4px;font-family:"Montserrat",Arial,sans-serif;font-weight:800;font-size:9px;color:var(--white);line-height:1.05;text-transform:uppercase}
.brand-mark{width:14px;height:14px;background:var(--white);flex:none}
.brand.on-light{color:var(--red)}
.brand.on-light .brand-mark{background:var(--red)}

.years{font-family:"Montserrat",Arial,sans-serif;font-weight:800;color:var(--white);text-align:center;line-height:1}
.years b{display:block;font-size:22px}
.years span{display:block;font-size:6px;font-weight:600;line-height:1.2}

.photo{position:absolute;border:2px solid var(--white)}
.photo.house{background:linear-gradient(180deg,var(--photo-sky) 0%,var(--photo-house-a) 45%,var(--photo-house-b) 100%)}
.photo.bare{border:none}

.tiny{font-size:5.5px;line-height:1.45}
.heading{font-family:"Montserrat",Arial,sans-serif;font-weight:800;text-transform:uppercase}

.logo-row{position:absolute;display:flex;gap:4px}
.logo-row i{display:block;width:16px;height:10px;background:var(--white)}

.name-band{position:absolute;left:0;right:0;background:var(--white);padding:6px 10px}
.service{position:absolute;left:0;right:0;text-align:center;font-family:"Montserrat",Arial,sans-serif;font-weight:800;font-size:8px;color:var(--white)}
</style>
</head>
<body>

<div class="view-label" style="left:96px">Folded outside</div>
<div class="view-label" style="left:372px">Folded inside</div>
<div class="view-label" style="left:838px">One sided front</div>
<div class="view-label" style="left:1044px">One sided back</div>

<section class="hanger" style="left:29px;width:120px">
  <div class="hanger-hole"></div>
  <div class="brand" style="position:absolute;left:10px;top:102px;font-size:7px">
    <span class="brand-mark" style="width:12px;height:12px"></span><span>Keystone<br>Builders</span>
  </div>
  <div class="years" style="position:absolute;right:10px;top:94px"><b>25</b><span>Years of<br>Excellence</span></div>
  <p class="heading" style="position:absolute;left:10px;right:8px;top:148px;font-size:7.5px;line-height:1.25">Building communities one home at a time</p>
  <p class="tiny" style="position:absolute;left:10px;right:8px;top:176px;font-weight:600">Keystone Builders brings 25 years of building experience to every project</p>
  <div class="photo house" style="left:10px;top:212px;width:52px;height:38px" role="img" aria-label="Photo of a finished brick home"></div>
  <div class="photo house" style="left:58px;top:228px;width:52px;height:38px" role="img" aria-label="Photo of a new roof on a family house"></div>
  <div class="photo house" style="left:22px;top:260px;width:60px;height:40px" role="img" aria-label="Photo of a restored two-storey home"></div>
  <div class="brand" style="position:absolute;left:10px;top:390px;font-size:7px">
    <span class="brand-mark" style="width:10px;height:10px"></span><span>Keystone Builders Ltd</span>
  </div>
  <p class="tiny" style="position:absolute;left:10px;top:406px">120 Harbour Road, Unit 4<br>Milton, ON L9T 2X1<br>Tel: 1-800-555-0142<br>ksbroofing.com</p>
  <div class="logo-row" style="left:10px;top:452px"><i></i><i></i><i></i><i></i></div>
</section>

<section class="hanger" style="left:149px;width:120px">
  <div class="hanger-hole"></div>
  <svg style="position:absolute;left:42px;top:98px" width="36" height="34" viewBox="0 0 36 34" fill="none" stroke="#fff" stroke-width="3" stroke-linejoin="round"><path d="M3 16 L18 3 L33 16"/><path d="M8 13 V31 H28 V13"/><rect x="15" y="19" width="6" height="6" fill="#fff" stroke="none"/></svg>
  <div class="name-band" style="top:180px">
    <div class="brand on-light" style="font-size:8.5px"><span class="brand-mark"></span><span>Keystone Builders Ltd</span></div>
  </div>
  <div class="service" style="top:222px">ROOFING &amp; RESTORATION</div>
  <div class="photo house bare" style="left:0;right:0;top:245px;height:235px" role="img" aria-label="Photo of a large brick house with a new roof"></div>
</section>

<section class="hanger" style="left:288px;width:276px">
  <div class="hanger-hole"></div>
  <div class="photo bare" style="left:0;right:0;top:0;height:178px;background:linear-gradient(180deg,#8a4a3a 0%,#a15c45 40%,#3f5a3c 75%,#6b8a4a 100%)" role="img" aria-label="Photo of a brick house front with green shutters and window boxes"></div>
  <div class="brand" style="position:absolute;left:12px;top:190px;font-size:10px">
    <span class="brand-mark" style="width:18px;height:18px"></span><span>Keystone<br>Builders Ltd</span>
  </div>
  <p class="tiny" style="position:absolute;left:122px;right:12px;top:186px">Keystone Builders Ltd. is the highest quality roof installation and repair firm in the region. We have provided superior roofing and restoration services to our customers for over twenty-five years.</p>
  <p class="heading" style="position:absolute;left:12px;top:238px;font-size:7px">Lorem ipsum dolor sit amet</p>
  <p class="tiny" style="position:absolute;left:12px;width:145px;top:250px">Sed ut perspiciatis unde omnis iste natus error sit voluptatem accusantium doloremque laudantium, totam rem aperiam eaque ipsa quae ab illo inventore veritatis et quasi architecto.</p>
  <div class="photo house" style="left:168px;top:236px;width:96px;height:120px" role="img" aria-label="Photo of a stone and brick home with a steep roof"></div>
  <p class="heading" style="position:absolute;left:12px;top:368px;font-size:7px">Lorem ipsum dolor sit amet</p>
  <p class="tiny" style="position:absolute;left:12px;right:12px;top:380px">Nemo enim ipsam voluptatem quia voluptas sit aspernatur aut odit aut fugit, sed quia consequuntur magni dolores eos qui ratione voluptatem sequi nesciunt neque porro quisquam est.</p>
  <div style="position:absolute;left:0;right:0;bottom:0;height:30px;background:var(--red-deep);display:flex;justify-content:space-between;align-items:center;padding:0 12px;font-family:'Montserrat',Arial,sans-serif;font-weight:700;font-size:8px">
    <span>Call Us: 1-800-555-0142</span><span>Or visit: ksbroofing.com</span>
  </div>
</section>

<section class="hanger" style="left:828px;width:137px">
  <div class="hanger-hole"></div>
  <svg style="position:absolute;left:14px;top:110px" width="30" height="28" viewBox="0 0 36 34" fill="none" stroke="#fff" stroke-width="3" stroke-linejoin="round"><path d="M3 16 L18 3 L33 16"/><path d="M8 13 V31 H28 V13"/><rect x="15" y="19" width="6" height="6" fill="#fff" stroke="none"/></svg>
  <div class="name-band" style="top:168px">
    <div class="brand on-light" style="font-size:9px"><span class="brand-mark"></span><span>Keystone Builders Ltd</span></div>
  </div>
  <div class="service" style="top:212px">ROOFING &amp; RESTORATION</div>
  <div class="photo house bare" style="left:0;right:0;top:232px;height:248px" role="img" aria-label="Photo of a large brick house with a new roof"></div>
  <div class="years" style="position:absolute;right:10px;top:370px;z-index:2"><b>25</b><span>Years of Excellence</span></div>
</section>

<section class="hanger" style="left:1032px;width:138px">
  <div class="hanger-hole"></div>
  <p class="heading" style="position:absolute;left:12px;top:92px;font-size:6.5px">Lorem ipsum dolor sit amet</p>
  <p class="tiny" style="position:absolute;left:12px;right:10px;top:102px">Ut enim ad minima veniam, quis nostrum exercitationem ullam corporis suscipit laboriosam, nisi ut aliquid ex ea commodi consequatur quis autem vel eum iure.</p>
  <p class="heading" style="position:absolute;left:12px;top:178px;font-size:6.5px">Lorem ipsum dolor sit amet</p>
  <p class="tiny" style="position:absolute;left:12px;right:10px;top:188px">Quis autem vel eum iure reprehenderit qui in ea voluptate velit esse quam nihil molestiae consequatur, vel illum qui dolorem eum fugiat quo voluptas nulla pariatur.</p>
  <p class="heading" style="position:absolute;left:12px;top:264px;font-size:6.5px">Lorem ipsum dolor sit amet</p>
  <p class="tiny" style="position:absolute;left:12px;right:10px;top:274px">At vero eos et accusamus et iusto odio dignissimos ducimus qui blanditiis praesentium voluptatum deleniti atque corrupti quos dolores et quas molestias.</p>
  <div class="logo-row" style="left:12px;top:382px"><i></i><i></i><i></i><i></i><i></i></div>
  <div class="brand" style="position:absolute;left:12px;top:404px;font-size:7px">
    <span class="brand-mark" style="width:10px;height:10px"></span><span>Keystone Builders Ltd</span>
  </div>
  <p class="tiny" style="position:absolute;left:12px;top:420px">120 Harbour Road, Unit 4<br>Milton, ON L9T 2X1<br>ksbroofing.com</p>
  <p class="heading" style="position:absolute;left:12px;top:456px;font-size:8px">Call: 1-800-555-0142</p>
</section>

</body>
</html>
```